A5 Flyer for Window Cleaning Company

2 sided Flyer design required for window cleaning company. One side to include we use traditional and hot water fed pole window cleaning systems, conservatory cleaning, and fascia and soffit cleaning. The other side to be for Gutter cleaning. See the must haves section of project brief for more info. Mixture of some images and text for both sides. ( do not have to use all images supplied). The flyer will be used to promote the business to new residential customers.

Target Market(s)

Private households/new customers

Industry/Entity Type

Window Cleaning

Font styles to use
Serif

Requirements
Must have
• Company address ( 7 Old Fenwick Court Marlow Lane Edinburgh EH14 8PJ
Phone numbers( 0131 642 7781 0800 218 5067).
Website and email address ( info@coral-window-cleaning.example)
Excellent Customer Service. Competitive prices. Established 1994.
Side 1of flyer = Coral Window Cleaning Side 2 of flyer Coral Gutter Cleaning.
Nice to have
• Professional look.

```html
<!DOCTYPE html>
<html lang="en">
<head>
<meta charset="utf-8">
<title>Coral Window Cleaning – A5 Flyer</title>
<link rel="stylesheet" href="https://fonts.googleapis.com/css2?family=Arimo:wght@700&family=Lato:wght@400;700&display=swap">
<style>
  :root {
    --navy: #0d1f5c;
    --sky: #6fa7dc;
    --white: #ffffff;
    --paper: #f4f4f4;
    --ink: #1b1b1b;
    --stage: #2e2e2e;
    --head: "Arimo", Arial, sans-serif;
    --body: "Lato", Helvetica, sans-serif;
  }
  * { box-sizing: border-box; margin: 0; padding: 0; }
  html, body { width: 902px; height: 1200px; overflow: hidden; background: var(--stage); }
  .sheet { position: relative; width: 902px; height: 1200px; }
  .flyer-slot { position: absolute; left: 40px; width: 822px; height: 586px; }
  .flyer-slot.front { top: 8px; }
  .flyer-slot.back { top: 606px; }
  .flyer {
    position: absolute; top: 0; left: 0;
    width: 612px; height: 436px;
    transform: scale(1.3431); transform-origin: 0 0;
    overflow: hidden; background: var(--white);
    font-family: var(--body); color: var(--ink);
  }
  .shapes { position: absolute; inset: 0; width: 612px; height: 436px; }
  .abs { position: absolute; }

  .brand-big {
    left: 314px; width: 298px; top: 36px; text-align: center;
    font-family: var(--head); font-weight: 700; font-size: 52px;
    color: var(--white); letter-spacing: 1px; line-height: 1;
  }
  .service-box {
    left: 332px; width: 261px; top: 99px; height: 37px;
    background: var(--navy); color: var(--white);
    font-family: var(--head); font-weight: 700; font-size: 22px;
    display: flex; align-items: center; justify-content: center;
  }
  .city {
    left: 314px; width: 298px; top: 143px; text-align: center;
    font-family: var(--head); font-weight: 700; font-size: 13px; color: var(--white);
  }
  .brand-mark {
    display: flex; flex-direction: column; align-items: center; gap: 5px;
    background: var(--white); text-align: center;
  }
  .brand-mark .square { width: 22px; height: 22px; background: var(--sky); }
  .brand-mark .name {
    font-family: var(--body); font-weight: 700; color: var(--navy);
    line-height: 1.15;
  }
  .front .brand-mark { left: 212px; top: 22px; width: 92px; height: 122px; justify-content: center; }
  .front .brand-mark .name { font-size: 14px; }
  .back .brand-mark { left: 20px; top: 330px; width: 63px; height: 82px; justify-content: center; gap: 4px; }
  .back .brand-mark .square { width: 16px; height: 16px; }
  .back .brand-mark .name { font-size: 10px; }

  .promises {
    left: 0; width: 312px; text-align: center;
    font-weight: 700; font-size: 11.5px; line-height: 17.5px; color: var(--ink);
  }
  .front .promises { top: 174px; }
  .back .promises { top: 170px; }

  .we-use-title { left: 43px; top: 234px; font-size: 8.5px; font-weight: 700; letter-spacing: .3px; }
  .we-use-list { left: 43px; top: 253px; list-style: none; font-size: 7.6px; line-height: 14px; }
  .we-use-list li { position: relative; padding-left: 18px; }
  .we-use-list li::before {
    content: ""; position: absolute; left: 0; top: 3.5px;
    width: 7px; height: 7px; border-radius: 50%; background: var(--navy);
  }

  .address {
    text-align: center; color: var(--white);
    font-size: 10.5px; line-height: 14.5px;
  }
  .front .address { left: 312px; width: 300px; top: 322px; }
  .back .address { left: 90px; width: 222px; top: 360px; }
  .pin { width: 12px; height: 14px; }
  .front .pin { left: 455px; top: 300px; }
  .back .pin { left: 195px; top: 338px; }

  .phone-row {
    left: 200px; top: 381px; width: 400px; display: flex; gap: 22px; align-items: center;
    font-family: var(--head); font-weight: 700; font-size: 19px; color: var(--white);
  }
  .phone-row span, .contact-line { display: flex; align-items: center; gap: 8px; }
  .icon { flex: none; }

  .intro {
    left: 18px; width: 280px; top: 233px;
    font-size: 8.5px; line-height: 11.7px; text-align: justify; color: #2a2a2a;
  }
  .intro p + p { margin-top: 7px; }

  .contact { left: 346px; top: 304px; color: var(--white); }
  .contact-title { font-family: var(--head); font-weight: 700; font-size: 9px; margin-bottom: 7px; }
  .contact-line.phone { font-family: var(--head); font-weight: 700; font-size: 15.5px; margin-bottom: 6px; }
  .contact-line.web { font-family: var(--head); font-weight: 700; font-size: 8.3px; margin-top: 8px; }

  .tag {
    top: 198px; height: 10px; padding: 0 5px; background: var(--white); color: var(--navy);
    font-family: var(--head); font-weight: 700; font-size: 6.5px; line-height: 10px;
  }
</style>
</head>
<body>
<main class="sheet">

  <!-- FRONT SIDE: windows -->
  <div class="flyer-slot front">
    <section class="flyer front" aria-label="Coral Window Cleaning flyer, front">
      <svg class="shapes" viewBox="0 0 612 436" aria-hidden="false">
        <defs>
          <linearGradient id="fPhotoTop" x1="0" y1="0" x2="1" y2="1">
            <stop offset="0" stop-color="#cdd6dc"/><stop offset=".5" stop-color="#e9edf0"/><stop offset="1" stop-color="#f7f7f7"/>
          </linearGradient>
          <linearGradient id="fPaper" x1="0" y1="0" x2="1" y2="0">
            <stop offset="0" stop-color="#ffffff"/><stop offset="1" stop-color="#e8e8e8"/>
          </linearGradient>
          <linearGradient id="fVan" x1="0" y1="0" x2="1" y2="0">
            <stop offset="0" stop-color="#8ec3ea"/><stop offset="1" stop-color="#d9ecf8"/>
          </linearGradient>
        </defs>
        <rect width="612" height="436" fill="url(#fPaper)"/>
        <g role="img" aria-label="Photo of a window cleaner washing a house window">
          <polygon points="0,0 315,0 315,160 157,150 0,166" fill="url(#fPhotoTop)"/>
        </g>
        <polygon points="314,0 612,0 612,155 458,176 314,155" fill="var(--sky)"/>
        <polyline points="0,168 157,151 314,163 458,180 612,160" fill="none" stroke="var(--navy)" stroke-width="5"/>
        <g role="img" aria-label="Photos of a cleaner at work, a conservatory, and a fascia being brushed">
          <polygon points="312,170 408,175 408,282 312,282" fill="#8a7d6e"/>
          <polygon points="408,175 510,178 510,282 408,282" fill="#b9b2a8"/>
          <polygon points="510,176 612,164 612,282 510,282" fill="#d7dadb"/>
        </g>
        <polygon points="312,280 612,266 612,436 312,436" fill="var(--navy)"/>
        <rect x="190" y="364" width="422" height="56" fill="var(--navy)"/>
        <rect x="0" y="420" width="612" height="16" fill="var(--white)"/>
        <rect x="312" y="420" width="300" height="16" fill="var(--navy)"/>
        <rect x="312" y="424" width="300" height="12" fill="var(--white)"/>
        <g role="img" aria-label="Photo of the company's branded blue van">
          <ellipse cx="108" cy="375" rx="85" ry="54" fill="url(#fVan)"/>
        </g>
      </svg>

      <div class="abs brand-mark"><span class="square"></span><span class="name">Coral Window Cleaning</span></div>
      <div class="abs brand-big">CORAL</div>
      <div class="abs service-box">WINDOW CLEANING</div>
      <div class="abs city">EDINBURGH</div>

      <div class="abs promises">Excellent Customer Service.<br>Competitive prices.<br>Established 1994.</div>
      <div class="abs we-use-title">WE USE</div>
      <ul class="abs we-use-list">
        <li>Traditional and hot water fed pole window cleaning systems</li>
        <li>Conservatory cleaning</li>
        <li>Fascia and soffit cleaning</li>
      </ul>

      <svg class="abs pin" viewBox="0 0 12 14" aria-hidden="true"><path d="M6 0a4.5 4.5 0 0 0-4.5 4.5C1.5 8 6 12 6 12s4.5-4 4.5-7.5A4.5 4.5 0 0 0 6 0zm0 6.5a2 2 0 1 1 0-4 2 2 0 0 1 0 4z" fill="#fff"/><rect x="2" y="13" width="8" height="1" fill="#fff"/></svg>
      <div class="abs address">7 Old Fenwick Court<br>Marlow Lane Edinburgh<br>EH14 8PJ</div>

      <div class="abs phone-row">
        <span><svg class="icon" width="20" height="14" viewBox="0 0 20 14" aria-hidden="true"><path d="M1 5c0-3 4-4 9-4s9 1 9 4l-3 1-1-2H5L4 6z" fill="#fff"/><path d="M5 6h10l3 7H2z" fill="#fff"/><circle cx="10" cy="9.5" r="2" fill="var(--navy)"/></svg>0131 642 7781</span>
        <span><svg class="icon" width="18" height="18" viewBox="0 0 18 18" aria-hidden="true"><circle cx="9" cy="9" r="8" fill="none" stroke="#fff" stroke-width="1.6"/><path d="M6 5l1.6-.2 1 2.2-.9.9c.5 1 1.3 1.8 2.3 2.3l.9-.9 2.2 1-.2 1.6c-3 .5-6.5-3-6.9-6.9z" fill="#fff"/></svg>0800 218 5067</span>
      </div>
    </section>
  </div>

  <!-- BACK SIDE: gutters -->
  <div class="flyer-slot back">
    <section class="flyer back" aria-label="Coral Gutter Cleaning flyer, back">
      <svg class="shapes" viewBox="0 0 612 436">
        <defs>
          <linearGradient id="bPhotoTop" x1="0" y1="0" x2="1" y2="1">
            <stop offset="0" stop-color="#8f9a7a"/><stop offset=".5" stop-color="#c7b79a"/><stop offset="1" stop-color="#e8e6e2"/>
          </linearGradient>
          <linearGradient id="bPaper" x1="0" y1="0" x2="1" y2="0">
            <stop offset="0" stop-color="#ffffff"/><stop offset="1" stop-color="#e6e6e6"/>
          </linearGradient>
        </defs>
        <rect width="612" height="436" fill="url(#bPaper)"/>
        <g role="img" aria-label="Photo of a gloved hand clearing autumn leaves from a gutter">
          <polygon points="0,0 315,0 315,165 157,150 0,166" fill="url(#bPhotoTop)"/>
        </g>
        <polygon points="314,0 612,0 612,165 458,185 314,168" fill="var(--sky)"/>
        <polyline points="0,168 157,152 314,170 458,188 612,168" fill="none" stroke="var(--navy)" stroke-width="5"/>
        <g role="img" aria-label="Before and after photos of a gutter being cleaned">
          <polygon points="312,174 458,192 458,292 312,292" fill="#6e7466"/>
          <polygon points="458,192 612,172 612,292 458,292" fill="#8b8f86"/>
        </g>
        <polygon points="312,290 612,276 612,436 312,436" fill="var(--navy)"/>
        <rect x="90" y="325" width="222" height="87" fill="var(--navy)"/>
      </svg>

      <div class="abs tag" style="left:420px">BEFORE</div>
      <div class="abs tag" style="left:470px">AFTER</div>

      <div class="abs brand-big">CORAL</div>
      <div class="abs service-box">GUTTER CLEANING</div>
      <div class="abs city" style="top:146px">EDINBURGH</div>

      <div class="abs promises">Excellent Customer Service.<br>Competitive prices.<br>Established 1994.</div>
      <div class="abs intro">
        <p>We specialise in serving the needs of homes that want the highest standards of cleaning at very competitive rates. As a result, a high percentage of our business is from repeat customers and referrals.</p>
        <p>All our staff are uniformed and carry Identification Cards at all times.</p>
      </div>

      <div class="abs brand-mark"><span class="square"></span><span class="name">Coral Window Cleaning</span></div>
      <svg class="abs pin" viewBox="0 0 12 14" aria-hidden="true"><path d="M6 0a4.5 4.5 0 0 0-4.5 4.5C1.5 8 6 12 6 12s4.5-4 4.5-7.5A4.5 4.5 0 0 0 6 0zm0 6.5a2 2 0 1 1 0-4 2 2 0 0 1 0 4z" fill="#fff"/><rect x="2" y="13" width="8" height="1" fill="#fff"/></svg>
      <div class="abs address">7 Old Fenwick Court<br>Marlow Lane Edinburgh<br>EH14 8PJ</div>

      <div class="abs contact">
        <div class="contact-title">CONTACT US :</div>
        <div class="contact-line phone"><svg class="icon" width="16" height="11" viewBox="0 0 20 14" aria-hidden="true"><path d="M1 5c0-3 4-4 9-4s9 1 9 4l-3 1-1-2H5L4 6z" fill="#fff"/><path d="M5 6h10l3 7H2z" fill="#fff"/><circle cx="10" cy="9.5" r="2" fill="var(--navy)"/></svg>0131 642 7781</div>
        <div class="contact-line phone"><svg class="icon" width="15" height="15" viewBox="0 0 18 18" aria-hidden="true"><circle cx="9" cy="9" r="8" fill="none" stroke="#fff" stroke-width="1.6"/><path d="M6 5l1.6-.2 1 2.2-.9.9c.5 1 1.3 1.8 2.3 2.3l.9-.9 2.2 1-.2 1.6c-3 .5-6.5-3-6.9-6.9z" fill="#fff"/></svg>0800 218 5067</div>
        <div class="contact-line web"><svg class="icon" width="13" height="9" viewBox="0 0 13 9" aria-hidden="true"><rect x=".5" y=".5" width="12" height="8" fill="none" stroke="#fff"/><path d="M.5.5l6 4.5 6-4.5" fill="none" stroke="#fff"/></svg>info@coral-window-cleaning.example</div>
        <div class="contact-line web"><svg class="icon" width="11" height="11" viewBox="0 0 11 11" aria-hidden="true"><circle cx="5.5" cy="5.5" r="5" fill="none" stroke="#fff"/><ellipse cx="5.5" cy="5.5" rx="2.2" ry="5" fill="none" stroke="#fff"/><path d="M.5 5.5h10" stroke="#fff"/></svg>www.coral-window-cleaning.example</div>
      </div>
    </section>
  </div>

</main>
</body>
</html>
```